Business Card for staff member of football club SC Brenval

I would like to get a business card template for all staff member of our soccer club.

The card should use as much as possible the 2 colors of the club : Red which is the main color and blue which is the alternative color. It can be balanced between the two like our logo.

I prefer simple and lean design.

Contact Information for Business Card

Bussiness card should have all main stuff as describe here below in must have.

Font styles to use
Sans Serif

Requirements
Must have
• Name : Laurent DESPRATIN
Fonction : Président
Mobile : +41 xx xxx xx xx
Email : first.lastname@scbrenval.ch
Adresse of the club : SC Brenval, 1873 Brenval
Website of the club : www.scbrenval.ch
Nice to have
• Version with and without picture of the staff member

A version for men, a version for women staff member.

```html
<!DOCTYPE html>
<html lang="fr">
<head>
<meta charset="utf-8">
<title>SC Brenval – Carte de visite</title>
<link rel="stylesheet" href="https://fonts.googleapis.com/css2?family=Poppins:wght@300;400;600;700&display=swap">
<style>
  :root {
    --club-red: #e0263f;
    --club-red-dark: #c51d34;
    --club-blue: #18a9d6;
    --ink: #231f20;
    --paper: #f4f4f4;
    --paper-shade: #e6e6e6;
    --stage: #d9d6d2;
    --white: #ffffff;
  }
  * { box-sizing: border-box; margin: 0; padding: 0; }
  html, body { width: 1200px; height: 780px; overflow: hidden; }
  body {
    background: var(--stage);
    font-family: "Poppins", sans-serif;
    position: relative;
  }
  .card {
    position: absolute;
    left: 300px;
    width: 600px;
    height: 343px;
    background: linear-gradient(160deg, var(--white), var(--paper) 60%, var(--paper-shade));
    overflow: hidden;
    box-shadow: 0 6px 18px rgba(0,0,0,.18);
  }
  .card--front { top: 27px; }
  .card--back { top: 410px; }

  .band-dark {
    position: absolute; left: 0; right: 0; top: 176px; height: 114px;
    background: var(--ink);
  }
  .band-rule {
    position: absolute; left: 0; right: 0; top: 290px; height: 4px;
    background: var(--white);
  }
  .band-red {
    position: absolute; left: 0; right: 0; top: 294px; bottom: 0;
    background: linear-gradient(90deg, var(--club-red), var(--club-red-dark));
    display: flex; align-items: center; padding-left: 36px;
  }

  .club-name {
    position: absolute;
    display: flex; align-items: center; gap: 10px;
    font-weight: 700; font-size: 32px; letter-spacing: -.5px;
    color: var(--ink);
  }
  .club-name__dot {
    width: 22px; height: 22px; border-radius: 50%;
    background: var(--club-red);
  }
  .card--front .club-name { right: 36px; top: 96px; }
  .card--back .club-name { left: 50%; top: 96px; transform: translateX(-50%); }

  .holder { position: absolute; left: 36px; top: 100px; }
  .holder__name { font-size: 22px; color: var(--ink); font-weight: 300; line-height: 1.1; }
  .holder__name strong { font-weight: 700; letter-spacing: .3px; }
  .holder__role { font-size: 12px; color: var(--club-red); margin-top: 3px; }

  .contacts {
    position: absolute; left: 36px; top: 192px;
    list-style: none; color: var(--white);
    font-size: 12px; line-height: 1;
  }
  .contacts li { display: flex; align-items: center; gap: 9px; height: 21px; }
  .contacts svg { width: 15px; height: 15px; flex: none; }

  .tagline {
    color: var(--white); font-size: 12px; letter-spacing: 2px;
  }
  .tagline strong { font-weight: 700; letter-spacing: 2.4px; }

  .website {
    color: rgba(255,255,255,.7); font-size: 12px; letter-spacing: 2px;
  }
</style>
</head>
<body>

<section class="card card--front" aria-label="Recto">
  <div class="club-name"><span class="club-name__dot"></span>SC Brenval</div>

  <div class="holder">
    <p class="holder__name">Laurent <strong>DESPRATIN</strong></p>
    <p class="holder__role">Président</p>
  </div>

  <div class="band-dark"></div>
  <ul class="contacts">
    <li>
      <svg viewBox="0 0 16 16"><circle cx="8" cy="8" r="8" fill="#e0263f"/><rect x="5.5" y="3.5" width="5" height="9" rx="1" fill="none" stroke="#fff" stroke-width="1.2"/></svg>
      +41 xx xxx xx xx
    </li>
    <li>
      <svg viewBox="0 0 16 16"><circle cx="8" cy="8" r="8" fill="#e0263f"/><rect x="4" y="5" width="8" height="6" fill="none" stroke="#fff" stroke-width="1.1"/><path d="M4 5l4 3.2L12 5" fill="none" stroke="#fff" stroke-width="1.1"/></svg>
      first.lastname@scbrenval.ch
    </li>
    <li>
      <svg viewBox="0 0 16 16"><circle cx="8" cy="8" r="8" fill="#e0263f"/><path d="M8 12.5s-3-3.2-3-5.3a3 3 0 0 1 6 0c0 2.1-3 5.3-3 5.3z" fill="#fff"/><circle cx="8" cy="7.2" r="1.1" fill="#e0263f"/></svg>
      SC Brenval, 1873 Brenval
    </li>
    <li>
      <svg viewBox="0 0 16 16"><circle cx="8" cy="8" r="8" fill="#e0263f"/><circle cx="8" cy="8" r="4" fill="none" stroke="#fff" stroke-width="1"/><path d="M4 8h8M8 4c-1.6 2.2-1.6 5.8 0 8M8 4c1.6 2.2 1.6 5.8 0 8" fill="none" stroke="#fff" stroke-width=".9"/></svg>
      www.scbrenval.ch
    </li>
  </ul>

  <div class="band-rule"></div>
  <div class="band-red">
    <p class="tagline"><strong>A CLUB, A FAMILY</strong> Founded in 1935</p>
  </div>
</section>

<section class="card card--back" aria-label="Verso">
  <div class="club-name"><span class="club-name__dot"></span>SC Brenval</div>
  <div class="band-dark"></div>
  <div class="band-rule"></div>
  <div class="band-red">
    <p class="website">www.scbrenval.ch</p>
  </div>
</section>

</body>
</html>
```